Letterhead designs for Property Management firm

Would like to see some different letterhead/envelope designs We are a residential property management company. We would like to see designs that utilize blue/grays/black

```html
<!DOCTYPE html>
<html lang="en">
<head>
<meta charset="utf-8">
<title>Harbourview Property Management – Letterhead</title>
<link href="https://fonts.googleapis.com/css2?family=Arimo:wght@400;700&display=swap" rel="stylesheet">
<style>
  :root {
    --blue: #1d4f9d;
    --ink: #2a2a2a;
    --paper: #ffffff;
  }
  html, body { margin: 0; padding: 0; overflow: hidden; background: var(--paper); }
  .letterhead {
    position: relative;
    width: 796px;
    height: 1200px;
    overflow: hidden;
    background: var(--paper);
    font-family: "Arimo", Arial, sans-serif;
    color: var(--ink);
  }
  .corner-band { position: absolute; display: block; }
  .corner-band--top { left: 0; top: 0; }
  .corner-band--bottom { right: 0; bottom: 0; }
  .brand {
    position: absolute;
    left: 462px;
    top: 160px;
    width: 256px;
    display: flex;
    align-items: center;
    gap: 10px;
    font-weight: 700;
    color: var(--blue);
  }
  .brand__mark { width: 20px; height: 20px; background: var(--blue); flex: none; }
  .brand__name { font-size: 22px; line-height: 1.15; letter-spacing: 0.5px; text-transform: uppercase; }
  .salutation { position: absolute; left: 74px; top: 308px; }
  .salutation__name { margin: 0; font-size: 33px; font-weight: 700; color: var(--ink); line-height: 1.1; }
  .salutation__role { margin: 7px 0 0 104px; font-size: 19px; font-weight: 400; color: var(--ink); }
  .letter-body {
    position: absolute;
    left: 77px;
    top: 405px;
    width: 650px;
    font-size: 16.2px;
    line-height: 18.1px;
    color: var(--ink);
  }
  .letter-body p { margin: 0 0 18px; }
  .letter-body .promo { margin-top: 36px; }
</style>
</head>
<body>
<div class="letterhead">
  <svg class="corner-band corner-band--top" width="640" height="200" viewBox="0 0 640 200" aria-hidden="true">
    <polygon points="0,0 620,0 0,190" fill="var(--blue)"/>
  </svg>
  <svg class="corner-band corner-band--bottom" width="500" height="150" viewBox="0 0 500 150" aria-hidden="true">
    <polygon points="500,10 500,150 0,150" fill="var(--blue)"/>
  </svg>

  <div class="brand">
    <span class="brand__mark"></span>
    <span class="brand__name">Harbourview<br>Property Management</span>
  </div>

  <header class="salutation">
    <h1 class="salutation__name">Dear Jhon Smith</h1>
    <p class="salutation__role">Manager Director</p>
  </header>

  <main class="letter-body">
    <p>His was not how Martin Hollis or Oliver Penrose would have scripted it. A feelgood movie about a veteran editor at the end of his career would have had the hero stepping down at the climax of his last and greatest campaign. The gnarled but lovable chief would write his final triumphalist headline before parading out of the office to a schmaltzy mix of applause and tears.</p>
    <p>And maybe that is how Paul Denholm imagined the end of his 26-year tenure of the Daily Courier. He would stay in the job just long enough to drive a final stake through the heart of Britain’s relationship with Europe. It would be the crowning moment of glory to round off a long and remarkable newspaper career.</p>
    <p>But for that script to work Denholm had to stay in post until at least November. He would steer the newspaper through the treacherous shifting sands of Brexit this autumn and be there to stiffen the spine of a weak prime minister who, on one view, owes her survival to Denholm’s patronage. Only then could he be certain that his life’s work was done.</p>
    <p class="promo">Sign up to the Press Digest: news for the news-makers<br>&nbsp;Read more<br>The choreography all pointed to that scenario. Helena Marsh attended a banquet in the City last November to celebrate Denholm’s quarter of a century at the Courier helm. And then, in June, came the announcement that Denholm would move upstairs to become chairman and editor-in-chief of Allied Newspapers. In November.</p>
    <p>But that script now appears to have been ripped up. Instead – and much more interestingly – Denholm will be now replaced by his colleague Gordon Grieve at the beginning of September. Only two months in it – except that Grieve’s instincts on Brexit are a million miles from Denholm’s and those two months will be nail-bitingly uncertain ones for any compulsive Brexiter. Who knows what turmoil, internecine warfare and backsliding could yet happen without Denholm to enforce discipline?</p>
    <p>Respect him or detest him – and both camps are well-subscribed – there’s no denying that Denholm has exercised an enormous influence on British politics and public life in his years as editor. His admirers put him in the same league as such celebrated and instinctive tabloid editors as Hugh Carrow of the Herald or Arthur Kristofsen of the Clarion. His detractors say he exerts power, both internally and externally, through intrusion, bullying and fear.</p>
  </main>
</div>
</body>
</html>
```